Flyer für Fußball-Feriencamps
Unglaublich tolle Arbeit - Vielen herzlichen Dank!
Zielgruppe
Die TRV-Academy ist eine unabhängige, junge und aufstrebende Akademie.
Wir entwickeln junge Spieler von U9 bis U19 in den bereichen Persönlichkeit, Mentale stärke und das Fußballerische Talent. Wir bieten Modernste und einzigartige Methoden sowie Konzepte.
Aufgabenstellung
Wir benötigen einen einheitlichen Flyer für alle unsere Fußball-Feriencamps.
Da wir mit verschiedenen Fußballvereinen Arbeiten, wäre es wichtig das es ein freies Feld gibt, wo wir dann im nachhinein die Termine drüber legen können.
Unser TRV Logo sollte auf den Flyer
In der Anlage ist ein Beispiel unseres alten Flyer als Beispiel in welche Richtung es gehe könnte.
Wir freuen uns auf kreative und innovative Ideen. :-)
folgende Begriffe sollten vorkommen: Koordination - Schnelligkeit - Technik - Spielintelligenz - Fitness
sowie: Mentale Leistungsfähigkeit - Selbstbewusstsein - Motivation - Soziale Kompetenzen
(Vielleicht auch in Pyramiden dargestellt?)
+ Training mit Modernsten Methoden und einzigartigen Technologien
Toll wäre auch, wenn folgendes irgendwo auftauchen würde: Konzentration verbessern - Motivation erhöhen - Mentale Leistung steigern - Selbstvertrauen stärken - Disziplin verbessern und mehr.
ganz unten vielleicht dann: Infos & Anmeldung unter: www.trv-academy.de

```html
<!DOCTYPE html>
<html lang="de">
<head>
<meta charset="utf-8">
<title>Fußball Feriencamp 2019 – TRV-Academy</title>
<link rel="stylesheet" href="https://fonts.googleapis.com/css2?family=Bungee&family=Encode+Sans:wght@600;700;800&display=swap">
<style>
  :root {
    --green-light: #dfe9e3;
    --green-mid: #6fbb86;
    --green-deep: #2f9a59;
    --green-dark: #07602f;
    --ink: #111111;
    --paper: #ffffff;
    --badge: #1d2a31;
    --ball-light: #f4f6f4;
    --ball-shade: #c9d3cc;
  }
  html, body {
    margin: 0;
    padding: 0;
    width: 846px;
    height: 1200px;
    overflow: hidden;
  }
  .flyer {
    position: relative;
    width: 846px;
    height: 1200px;
    overflow: hidden;
    background:
      radial-gradient(ellipse 700px 520px at 8% 0%, rgba(240,243,242,0.95), rgba(240,243,242,0) 70%),
      linear-gradient(172deg, var(--green-light) 0%, #b9dcc0 18%, var(--green-mid) 45%, var(--green-deep) 72%, var(--green-dark) 100%);
    font-family: "Encode Sans", Arial, sans-serif;
  }
  .headline {
    position: absolute;
    left: 58px;
    margin: 0;
    font-family: "Bungee", Impact, sans-serif;
    font-weight: 400;
    line-height: 1;
  }
  .headline--year {
    top: 60px;
    font-size: 98px;
    color: var(--ink);
    letter-spacing: -2px;
  }
  .headline--title {
    top: 158px;
    font-size: 72px;
    color: var(--paper);
    line-height: 79px;
    letter-spacing: -1px;
  }
  .brand-badge {
    position: absolute;
    left: 590px;
    top: 50px;
    width: 214px;
    height: 214px;
    border-radius: 50%;
    background: var(--badge);
    display: flex;
    align-items: center;
    justify-content: center;
    color: var(--paper);
    font-family: "Encode Sans", Arial, sans-serif;
    font-weight: 800;
    font-size: 28px;
    text-align: center;
    line-height: 1.1;
  }
  .date-field {
    position: absolute;
    left: 0;
    top: 0;
  }
  .promise {
    position: absolute;
    left: 520px;
    top: 444px;
    width: 300px;
    margin: 0;
    text-align: center;
    color: var(--paper);
    font-weight: 700;
    font-size: 38px;
    line-height: 44px;
    text-shadow: 0 0 8px rgba(0,70,30,0.45);
  }
  .ball {
    position: absolute;
    left: 632px;
    top: 792px;
    width: 344px;
    height: 344px;
    border-radius: 50%;
    background: radial-gradient(circle at 45% 40%, var(--ball-light) 0%, #e6ebe7 55%, var(--ball-shade) 100%);
    box-shadow: 0 0 18px rgba(0,0,0,0.25);
  }
  .skills {
    position: absolute;
    left: 0;
    top: 0;
  }
  .skills text {
    font-family: "Encode Sans", Arial, sans-serif;
    font-weight: 700;
    font-size: 22px;
    fill: var(--ink);
  }
  .footer-cta {
    position: absolute;
    left: 0;
    width: 846px;
    top: 1125px;
    margin: 0;
    text-align: center;
    color: var(--paper);
    font-weight: 700;
    font-size: 27px;
  }
</style>
</head>
<body>
<main class="flyer">
  <h1 class="headline headline--year">2019!</h1>
  <h2 class="headline headline--title">FUSSBALL<br>FERIENCAMP</h2>

  <div class="brand-badge">TRV<br>Academy</div>

  <svg class="date-field" width="846" height="1200" viewBox="0 0 846 1200" aria-label="Freies Feld für Camp-Termine">
    <polygon points="60,508 140,498 230,455 330,440 420,408 470,402 505,440 512,700 500,735 440,740 300,750 110,760 68,690 50,560" fill="#ffffff"/>
    <rect x="128" y="425" width="313" height="313" fill="#ffffff" stroke="#231f20" stroke-width="10"/>
  </svg>

  <p class="promise">Training mit modernsten Methoden und einzigartigen Technologien</p>

  <div class="ball" role="img" aria-label="Fußball"></div>

  <svg class="skills" width="846" height="1200" viewBox="0 0 846 1200">
    <g fill="#ffffff">
      <polygon points="0,819 293,819 254,867 0,867"/>
      <polygon points="0,873 327,873 290,921 0,921"/>
      <polygon points="0,926 360,926 327,974 34,974"/>
      <polygon points="36,979 397,979 363,1027 68,1027"/>
      <polygon points="71,1032 434,1032 400,1080 102,1080"/>

      <polygon points="285,819 579,819 546,867 300,867"/>
      <polygon points="313,873 610,873 577,921 332,921"/>
      <polygon points="347,926 640,926 609,974 363,974"/>
      <polygon points="379,979 671,979 640,1027 392,1027"/>
      <polygon points="413,1032 700,1032 669,1080 421,1080"/>
    </g>
    <text x="26" y="851">Motivation erhöhen</text>
    <text x="48" y="904">Disziplin verbessern</text>
    <text x="69" y="957">Selbstvertrauen stärken</text>
    <text x="88" y="1010">Mentale Leistung steigern</text>
    <text x="120" y="1063">Konzentration verbessern</text>

    <text x="321" y="851">KOORDINATION</text>
    <text x="344" y="904">SCHNELLIGKEIT</text>
    <text x="384" y="957">TECHNIK</text>
    <text x="411" y="1010">SPIELINTELLIGENZ</text>
    <text x="447" y="1063">FITNESS</text>
  </svg>

  <p class="footer-cta">Infos &amp; Anmeldung unter: www.trv-academy.de</p>
</main>
</body>
</html>
```